Healthcare food company need product packaging design

We need a food supplements product packaging design for an all natural wholesome food.
For natural wholesome design, we need a fresh and clean looking label as the products contain soybean, kale and broccoli as an alternative protein food powder. To appeal to the health conscious consumer .

Target Market(s)

For natural wholesome food, all age group

Industry/Entity Type

Health And Wellness

Font styles to use
Serif
Sans Serif

Requirements
Must have
• Strong colours and bigger font size to attract consumer when product is placed on shelf
Nice to have
• Fresh vegetable colours with elements of green or mutiple colours
Should not have
• No restriction

```html
<!DOCTYPE html>
<html lang="en">
<head>
<meta charset="utf-8">
<title>All Plant Source Protein Powder – Label</title>
<link href="https://fonts.googleapis.com/css2?family=Nunito+Sans:wght@400;600;800;900&family=Lato:wght@400;700&display=swap" rel="stylesheet">
<style>
  :root {
    --page-bg: #eef0ea;
    --label-white: #ffffff;
    --leaf-green: #8cb43a;
    --leaf-green-light: #a9cb52;
    --leaf-green-dark: #5f8a24;
    --ink: #2b211c;
    --ink-soft: #4a4440;
    --rule-grey: #7a7a7a;
    --berry: #c0185a;
    --berry-dark: #9c1048;
    --cobalt: #3f6fb8;
    --kale-deep: #4f8a2a;
    --kale-light: #9fcf55;
  }
  * { margin: 0; padding: 0; box-sizing: border-box; }
  html, body {
    width: 1150px;
    height: 1200px;
    overflow: hidden;
    background: var(--page-bg);
  }
  .canvas {
    position: relative;
    width: 1150px;
    height: 1200px;
  }
  .label {
    position: absolute;
    left: 50px;
    top: 190px;
    width: 1050px;
    height: 820px;
    background: var(--label-white);
    overflow: hidden;
    box-shadow: 0 2px 14px rgba(0,0,0,0.08);
  }
  .band-top {
    position: absolute;
    left: 0; top: 0;
    width: 100%; height: 75px;
    background: linear-gradient(180deg, var(--leaf-green-light), var(--leaf-green));
  }
  .band-bottom {
    position: absolute;
    left: 0; top: 704px;
    width: 100%; height: 116px;
    background: linear-gradient(180deg, var(--leaf-green), var(--leaf-green-light));
  }
  .net-weight {
    position: absolute;
    left: 160px;
    top: 744px;
    width: 320px;
    text-align: center;
    font-family: "Lato", sans-serif;
    font-weight: 400;
    font-size: 38px;
    color: var(--label-white);
  }
  .kicker {
    position: absolute;
    left: 33px;
    top: 110px;
    font-family: "Nunito Sans", sans-serif;
    font-weight: 600;
    font-size: 31px;
    letter-spacing: 0.5px;
    color: var(--ink-soft);
  }
  .title {
    position: absolute;
    left: 28px;
    top: 140px;
    font-family: "Nunito Sans", sans-serif;
    font-weight: 900;
    color: var(--ink);
    line-height: 0.92;
  }
  .title-line-1 { display: block; font-size: 98px; letter-spacing: -1px; }
  .title-line-2 { display: block; font-size: 120px; letter-spacing: -2px; }
  .title-rule {
    position: absolute;
    left: 33px;
    top: 347px;
    width: 440px;
    height: 4px;
    background: var(--rule-grey);
  }
  .ingredients {
    position: absolute;
    left: 33px;
    top: 375px;
    font-family: "Lato", sans-serif;
    font-size: 28px;
    line-height: 1.45;
    color: var(--ink-soft);
  }
  .produce-visual {
    position: absolute;
    left: 650px;
    top: 360px;
    width: 380px;
    height: 340px;
  }
  .brand {
    position: absolute;
    left: 14px;
    top: 585px;
    width: 130px;
    text-align: center;
  }
  .brand-dot {
    display: block;
    margin: 0 auto 8px;
    width: 72px;
    height: 72px;
    border-radius: 50%;
    background: var(--leaf-green-dark);
  }
  .brand-name {
    font-family: "Nunito Sans", sans-serif;
    font-weight: 800;
    font-size: 19px;
    color: var(--leaf-green-dark);
    white-space: nowrap;
  }
  .badge-bcaa {
    position: absolute;
    left: 158px;
    top: 618px;
    width: 86px;
    height: 78px;
    border-radius: 6px;
    background: linear-gradient(180deg, var(--berry), var(--berry-dark));
    color: var(--label-white);
    font-family: "Nunito Sans", sans-serif;
    font-weight: 800;
    text-align: center;
    padding-top: 8px;
    line-height: 1.05;
  }
  .badge-bcaa .amount { display: block; font-size: 29px; }
  .badge-bcaa .unit { display: block; font-size: 22px; }
  .pill {
    position: absolute;
    left: 254px;
    border-radius: 5px;
    background: var(--cobalt);
    color: var(--label-white);
    font-family: "Nunito Sans", sans-serif;
    font-weight: 800;
    display: flex;
    align-items: center;
    justify-content: center;
    gap: 6px;
    white-space: nowrap;
  }
  .pill-serving {
    top: 618px;
    width: 112px;
    height: 30px;
    font-size: 13px;
  }
  .pill-glutamine {
    top: 656px;
    width: 112px;
    height: 40px;
  }
  .pill-glutamine .amount { font-size: 24px; }
  .pill-glutamine .unit { font-size: 12px; }
</style>
</head>
<body>
<div class="canvas">
  <section class="label">
    <div class="band-top"></div>

    <p class="kicker">ALL PLANT SOURCE</p>
    <h1 class="title">
      <span class="title-line-1">protein</span>
      <span class="title-line-2">powder</span>
    </h1>
    <div class="title-rule"></div>

    <p class="ingredients">Kale, Soy Bean<br>powder, Pea Powder,<br>Lecithin</p>

    <svg class="produce-visual" viewBox="0 0 380 340" role="img" aria-label="Photograph of fresh curly green kale leaves">
      <defs>
        <radialGradient id="kaleTone" cx="45%" cy="40%" r="65%">
          <stop offset="0%" stop-color="var(--kale-light)"/>
          <stop offset="100%" stop-color="var(--kale-deep)"/>
        </radialGradient>
      </defs>
      <ellipse cx="200" cy="170" rx="175" ry="160" fill="url(#kaleTone)"/>
    </svg>

    <div class="brand">
      <span class="brand-dot"></span>
      <span class="brand-name">Verda Vale</span>
    </div>

    <div class="badge-bcaa">
      <span class="amount">5.5g</span>
      <span class="unit">BCAAs</span>
    </div>
    <div class="pill pill-serving">*PER SERVING</div>
    <div class="pill pill-glutamine">
      <span class="amount">4g</span>
      <span class="unit">GLUTAMINE</span>
    </div>

    <div class="band-bottom"></div>
    <p class="net-weight">Net Wt. 300gr</p>
  </section>
</div>
</body>
</html>
```